National Mission Critical Construction Contractor needs Stationery Design to make a bold statement

We are a small commercial construction company, working primarily in mission critical facilities across the U.S.. We have exciting corporate changes going an and a new logo and office space so we need new stationery. The final design should incorporate our new logo and invoke a fresh, high-tech feel while looking simple and modern.

Industry/Entity Type

Construction

Contact Information for Business Card

We are required to list our state licensing qualifications on the back of our card.

Font styles to use
Sans Serif

Requirements
Must have
• We need to have a design for second page of stationery, envelopes both standard and with a window and for a 3 x 4 notepad.

```html
<!DOCTYPE html>
<html lang="en">
<head>
<meta charset="utf-8">
<title>Stonebridge Construction Management – Envelope</title>
<link href="https://fonts.googleapis.com/css2?family=Open+Sans:wght@400;600&display=swap" rel="stylesheet">
<style>
  :root {
    --bg: #e4e4e1;
    --paper: #f3f3f1;
    --green: #7db23a;
    --sky: #2a97d0;
    --navy: #1168ad;
    --ink: #1a5f9e;
  }
  * { margin: 0; padding: 0; box-sizing: border-box; }
  html, body {
    width: 1200px; height: 900px; overflow: hidden;
    background: var(--bg);
    font-family: "Open Sans", Arial, sans-serif;
  }
  .envelope {
    position: absolute; left: 100px; top: 220px;
    width: 1000px; height: 460px;
    background: var(--paper);
    box-shadow: 0 2px 10px rgba(0,0,0,0.12);
    overflow: hidden;
  }
  .corner-art {
    position: absolute; left: 0; top: 0;
    width: 720px; height: 130px;
    background: linear-gradient(100deg, var(--green) 0%, var(--green) 40%, var(--sky) 80%, var(--navy) 100%);
  }
  .base-band {
    position: absolute; left: 0; right: 0; bottom: 10px;
    height: 14px; background: var(--navy);
  }
  .brand {
    position: absolute; left: 0; right: 0; top: 160px;
    text-align: center; color: var(--ink); font-weight: 600;
  }
  .brand-mark {
    display: block; width: 54px; height: 54px; margin: 0 auto 10px;
    border: 4px solid var(--ink); border-radius: 50%;
  }
  .brand-name { font-size: 30px; letter-spacing: 1px; line-height: 1; }
  .brand-tagline {
    display: inline-block; margin-top: 6px; padding-top: 4px;
    border-top: 1.5px solid var(--ink);
    font-size: 10px; letter-spacing: 2.2px;
  }
  .contact {
    position: absolute; display: flex; align-items: center; gap: 6px;
    color: var(--ink); font-size: 14px; white-space: nowrap;
  }
  .contact svg { width: 16px; height: 16px; fill: var(--ink); }
  .contact .divider { width: 1.5px; height: 16px; background: var(--ink); }
  .contact-address { left: 40px; bottom: 34px; }
  .contact-phone { left: 0; right: 0; bottom: 34px; justify-content: center; }
  .contact-email { right: 40px; bottom: 34px; }
</style>
</head>
<body>
  <main class="envelope">
    <div class="corner-art" role="img" aria-label="Decorative green and blue sweeping band artwork across the top left corner"></div>
    <div class="base-band"></div>

    <div class="brand">
      <span class="brand-mark"></span>
      <div class="brand-name">STONEBRIDGE</div>
      <div class="brand-tagline">CONSTRUCTION MANAGEMENT</div>
    </div>

    <div class="contact contact-address">
      <svg viewBox="0 0 16 16"><path d="M1 3h14v10H1z M2.5 4.5v.3L8 9l5.5-4.2v-.3z M2.5 6.6v4.9h11V6.6L8 10.8z" fill-rule="evenodd"/></svg>
      <span class="divider"></span>
      <span>418 street sparks, nevada</span>
    </div>

    <div class="contact contact-phone">
      <svg viewBox="0 0 16 16"><circle cx="8" cy="8" r="8"/><path fill="#fff" d="M5 4.2l1.6-.2.8 2-1 .8a5.5 5.5 0 0 0 2.8 2.8l.8-1 2 .8-.2 1.6c-.2.5-.8.8-1.3.7A7 7 0 0 1 4.3 5.5c-.1-.5.2-1.1.7-1.3z"/></svg>
      <span class="divider"></span>
      <span>(555)-014-7720</span>
    </div>

    <div class="contact contact-email">
      <svg viewBox="0 0 16 16"><path d="M8 1a5 5 0 0 0-5 5c0 3.8 5 9 5 9s5-5.2 5-9a5 5 0 0 0-5-5zm0 7a2 2 0 1 1 0-4 2 2 0 0 1 0 4z"/></svg>
      <span class="divider"></span>
      <span>stonebridge@mailbox.co</span>
    </div>
  </main>
</body>
</html>
```